Trifold A4 doublesided flyer/brochure and possibly logo redisgn for Qorvel Vending solutions

We are a Sydney based drink and snack vending machine company that supply maintain and restock free vending machines for Sydney businesses. Most our sites are office work places as well as some training organizations and a gym. We require a Trifold A4 double sided flyer/brochure we can letterbox drop to local businesses that have a large amount of staff and would benefit from a vending machine in there staff lunchroom. We would also like to use the flyer for larger businesses that may have a showroom for there own customers.
The flyer needs to look sophisticated modern and professional and immediately convey the offer of a fully installed serviced and maintained vending machine absolutely FREE.
Also needs to include
Vending machine features
Our large range of products especially healthy options
Our ongoing support and servicing and commitment to superior service
We essentially dont have a logo so some sort of logo design would be a bonus
I am trying to look for high quality pictures suitable for print but i am finding it difficult.
I will keep searching and post soon.
We would like the original document or the general background as well so we can modify or add new text later our self resend a different version of the flyer
Our website has some pictures but they are not good enough for print.
www.qorvelindustries.com.au
We can use the main elements form the website but does not need to look the same or use the same fonts. you can give any thing a try although it would be good to tie in

Requirements
Must have
• I have uploaded a word document with some content and some pictures.
Pictures can be used at your discretion. you dont have to use these

```html
<!DOCTYPE html>
<html lang="en">
<head>
<meta charset="utf-8">
<title>Qorvel Vending Solutions – Trifold Brochure</title>
<link rel="stylesheet" href="https://fonts.googleapis.com/css2?family=Roboto+Condensed:ital,wght@0,700;1,700;1,800&family=Open+Sans:wght@400;600&display=swap">
<style>
  :root{
    --bg:#e7e5e1;
    --red:#b8141d;
    --red-dark:#7a0a10;
    --red-light:#d8262e;
    --ink:#1c1c1e;
    --slate:#2d2e31;
    --steel:#4a4c50;
    --paper:#f4f1ea;
    --mint:#8fcfc4;
    --white:#ffffff;
    --muted:#c9c9cc;
  }
  *{box-sizing:border-box;margin:0;padding:0}
  html,body{width:1200px;height:1000px;overflow:hidden}
  body{background:var(--bg);font-family:"Open Sans",Arial,sans-serif;color:var(--white);position:relative}

  .sheet{position:absolute;width:660px;height:467px;display:flex;box-shadow:0 6px 18px rgba(0,0,0,.25)}
  .sheet--outside{left:40px;top:22px}
  .sheet--inside{left:500px;top:505px}
  .sheet--folded{left:40px;top:505px;width:220px}

  .panel{position:relative;width:220px;height:100%;overflow:hidden;
    background:linear-gradient(160deg,var(--steel) 0%,var(--slate) 35%,var(--ink) 100%)}
  .panel + .panel{border-left:1px solid rgba(0,0,0,.35)}

  .photo{position:absolute;display:block}

  .heading{font-family:"Roboto Condensed",Arial,sans-serif;font-weight:800;font-style:italic;
    text-transform:uppercase;font-size:10px;letter-spacing:.3px;line-height:1.15;color:var(--white)}
  .body-text{font-size:6.4px;line-height:1.55;color:#e6e6e8}
  .tag{display:inline-block;background:var(--red);padding:3px 6px;border-left:3px solid var(--red-light)}

  /* brand name block */
  .brand{position:absolute;display:flex;align-items:center;gap:7px;
    font-family:"Roboto Condensed",Arial,sans-serif;font-weight:700;color:var(--white);text-transform:uppercase}
  .brand__mark{width:12px;height:12px;background:var(--red)}
  .brand__name{line-height:1}

  /* cover */
  .cover .brand{left:18px;top:22px;font-size:19px}
  .cover .brand__mark{width:16px;height:16px}
  .cover .machine{left:26px;top:70px;width:168px;height:150px;border-radius:3px;
    background:linear-gradient(180deg,#b9bcc2 0%,#5a5d63 18%,#1a1b1d 60%,#3a3c40 100%);
    box-shadow:0 0 0 3px #8d9096}
  .cover .swoosh{position:absolute;left:0;top:200px;width:220px;height:267px}
  .cover .tagline{position:absolute;left:14px;right:14px;top:340px;
    font-family:"Roboto Condensed",Arial,sans-serif;font-weight:700;font-style:italic;
    text-transform:uppercase;font-size:8px;line-height:1.3;text-align:right}
  .phone{font-family:"Roboto Condensed",Arial,sans-serif;font-weight:800;font-style:italic;
    font-size:25px;letter-spacing:.5px;color:var(--white)}
  .web{font-family:"Roboto Condensed",Arial,sans-serif;font-weight:700;font-size:9.5px;color:var(--white)}
  .cover .phone{position:absolute;right:14px;top:378px}
  .cover .web{position:absolute;right:14px;top:412px}

  /* outside left: machines & payment */
  .machines .heading{position:absolute;left:14px;top:18px;font-size:11px}
  .machines .body-text{position:absolute;left:14px;right:14px;top:36px}
  .machines .gym{left:0;top:120px;width:220px;height:140px;
    background:linear-gradient(135deg,#dfe4ea 0%,#9aa6b3 45%,#4a5563 100%)}
  .pay{position:absolute;left:0;top:260px;width:220px;height:207px;background:var(--paper);color:var(--ink);padding:12px 12px}
  .pay__title{font-family:"Roboto Condensed",Arial,sans-serif;font-weight:800;font-style:italic;
    font-size:22px;line-height:.9;color:var(--mint);text-transform:lowercase}
  .pay__title span{color:#3b7f8e}
  .pay__options{display:flex;gap:6px;margin-top:10px}
  .pay__option{flex:1;border:1.5px solid #3b7f8e;text-align:center;padding:4px 2px}
  .pay__option b{display:block;background:#3b7f8e;color:var(--white);font-family:"Roboto Condensed",Arial,sans-serif;
    font-size:8px;text-transform:uppercase;padding:2px 0;margin-bottom:4px}
  .pay__option small{font-size:5.6px;color:#444}
  .pay__cards{display:flex;gap:8px;margin-top:12px;align-items:center}
  .card-shape{width:44px;height:28px;border-radius:3px}
  .card-shape--a{background:#23337a}
  .card-shape--b{background:#d99a2b}
  .pay__note{margin-left:auto;background:var(--red);color:var(--white);font-size:6px;font-weight:600;padding:5px 6px;text-transform:uppercase}
  .pay__step{margin-top:10px;display:flex;gap:6px;align-items:center;font-size:6px;color:#333}
  .pay__step i{font-style:normal;font-family:"Roboto Condensed",Arial,sans-serif;font-weight:800;font-size:13px;color:#3b7f8e}

  /* outside middle: support */
  .support .top-band{position:absolute;left:0;top:0;width:220px;height:150px;
    background:linear-gradient(180deg,var(--ink) 0%,var(--slate) 100%)}
  .support .red-field{position:absolute;left:0;top:150px;width:220px;height:317px;
    background:linear-gradient(180deg,var(--red) 0%,var(--red-dark) 100%)}
  .support .block{position:absolute;left:14px;right:14px}
  .support .block--a{top:160px}
  .support .block--b{top:238px}
  .support .block .body-text{margin-top:5px;color:#fbe9ea}
  .support .divider{position:absolute;left:14px;right:14px;top:228px;height:1px;background:rgba(255,255,255,.4)}
  .ticks{position:absolute;left:14px;top:312px;list-style:none}
  .ticks li{display:flex;align-items:center;gap:5px;font-size:6.6px;margin-bottom:5px}
  .support .brand{left:132px;top:418px;font-size:14px}

  /* inside left */
  .offer .hand{left:0;top:0;width:220px;height:150px;
    background:linear-gradient(160deg,#c7ccd3 0%,#7c8591 50%,#2b2e33 100%)}
  .offer .section{position:absolute;left:12px;right:12px}
  .offer .section--a{top:160px}
  .offer .section--b{top:270px}
  .section .body-text{margin-top:6px}
  .offer .brand{left:14px;top:418px;font-size:16px}

  /* inside middle */
  .range .office{left:0;top:0;width:220px;height:160px;
    background:linear-gradient(180deg,#5d7a6e 0%,#9aa7a4 45%,#d9dcdc 100%)}
  .range .section{position:absolute;left:12px;right:12px}
  .range .section--a{top:172px}
  .range .section--b{top:290px}

  /* inside right */
  .free .tag{position:absolute;left:10px;right:10px;top:14px;font-size:8.2px}
  .free .team{left:14px;top:52px;width:192px;height:170px;
    background:linear-gradient(160deg,#e7e7ea 0%,#8a8e96 40%,#1d1e21 100%)}
  .free .swoosh{position:absolute;left:0;top:215px;width:220px;height:252px}
  .free .phone{position:absolute;right:14px;top:360px}
  .free .web{position:absolute;right:14px;top:394px}
</style>
</head>
<body>

<!-- Outside of the trifold -->
<section class="sheet sheet--outside" aria-label="Brochure outside">
  <article class="panel machines">
    <h2 class="heading">Our Machines</h2>
    <p class="body-text">Qorvel Vending offers a modern range of snack and drink machines to suit any work place. Each unit has bright displays, chilled storage and easy payment options, and we tailor the product mix to the needs of your staff and visitors.</p>
    <div class="photo gym" role="img" aria-label="Photo of people exercising in a gym beside a vending machine"></div>
    <div class="pay">
      <p class="pay__title">three <span>ways to pay</span></p>
      <div class="pay__options">
        <div class="pay__option"><b>Cards</b><small>Tap or insert card</small></div>
        <div class="pay__option"><b>Notes</b><small>Notes accepted</small></div>
        <div class="pay__option"><b>Coins</b><small>Exact or change</small></div>
      </div>
      <div class="pay__cards">
        <div class="card-shape card-shape--a" aria-hidden="true"></div>
        <div class="card-shape card-shape--b" aria-hidden="true"></div>
        <span class="pay__note">No surcharge applies</span>
      </div>
      <div class="pay__step"><i>A</i> Choose your item</div>
      <div class="pay__step"><i>B</i> Pay your way</div>
    </div>
  </article>

  <article class="panel support">
    <div class="top-band"></div>
    <div class="red-field"></div>
    <div class="block block--a">
      <h2 class="heading">24 Hour Support</h2>
      <p class="body-text">Our team is on call day and night. If a machine has a fault, one phone call is all it takes and a technician will be with you fast to get it running again.</p>
    </div>
    <div class="divider"></div>
    <div class="block block--b">
      <h2 class="heading">Regular Stocking<br>and Servicing</h2>
      <p class="body-text">Trained staff visit on a set schedule to restock, clean and check every machine, so your shelves stay full and fresh without you lifting a finger.</p>
    </div>
    <ul class="ticks">
      <li><svg width="8" height="8" viewBox="0 0 8 8"><path d="M1 4.2 3 6.2 7 1.6" fill="none" stroke="#fff" stroke-width="1.4"/></svg>Reduce your carbon footprint</li>
      <li><svg width="8" height="8" viewBox="0 0 8 8"><path d="M1 4.2 3 6.2 7 1.6" fill="none" stroke="#fff" stroke-width="1.4"/></svg>Low energy machines at no cost</li>
    </ul>
    <div class="brand"><span class="brand__mark"></span><span class="brand__name">Qorvel</span></div>
  </article>

  <article class="panel cover">
    <div class="brand"><span class="brand__mark"></span><span class="brand__name">Qorvel<br>Vending Solutions</span></div>
    <div class="photo machine" role="img" aria-label="Photo of a snack and coffee vending machine"></div>
    <svg class="swoosh" viewBox="0 0 220 267" preserveAspectRatio="none" aria-hidden="true">
      <path d="M0 60 Q110 -10 220 30 L220 267 L0 267 Z" fill="var(--red)"/>
      <path d="M0 60 Q110 -10 220 30 L220 40 Q110 5 0 72 Z" fill="var(--red-light)"/>
    </svg>
    <p class="tagline">Specialising in free vending machines<br>for Sydney based businesses</p>
    <p class="phone">1300 555 019</p>
    <p class="web">www.qorvelindustries.com.au</p>
  </article>
</section>

<!-- Folded brochure showing the cover -->
<section class="sheet sheet--folded" aria-label="Folded brochure cover">
  <article class="panel cover">
    <div class="brand"><span class="brand__mark"></span><span class="brand__name">Qorvel<br>Vending Solutions</span></div>
    <div class="photo machine" role="img" aria-label="Photo of a snack and coffee vending machine"></div>
    <svg class="swoosh" viewBox="0 0 220 267" preserveAspectRatio="none" aria-hidden="true">
      <path d="M0 60 Q110 -10 220 30 L220 267 L0 267 Z" fill="var(--red)"/>
      <path d="M0 60 Q110 -10 220 30 L220 40 Q110 5 0 72 Z" fill="var(--red-light)"/>
    </svg>
    <p class="tagline">Specialising in free vending machines<br>for Sydney based businesses</p>
    <p class="phone">1300 555 019</p>
    <p class="web">www.qorvelindustries.com.au</p>
  </article>
</section>

<!-- Inside of the trifold -->
<section class="sheet sheet--inside" aria-label="Brochure inside">
  <article class="panel offer">
    <div class="photo hand" role="img" aria-label="Photo of a hand choosing an item at a vending machine"></div>
    <div class="section section--a">
      <h2 class="heading tag">Receive a free vending machine<br>for your work place</h2>
      <p class="body-text">Qorvel Vending will place a new machine in your office at no charge. We deliver, install and fill it, then keep it serviced for as long as you like. There are no contracts, no rental and no hidden costs.</p>
    </div>
    <div class="section section--b">
      <h2 class="heading tag">Customized vending solutions</h2>
      <p class="body-text">Every site is different. We look at your staff numbers, hours and tastes, then choose the right machine and product range so your team gets exactly what they want each day.</p>
    </div>
    <div class="brand"><span class="brand__mark"></span><span class="brand__name">Qorvel</span></div>
  </article>

  <article class="panel range">
    <div class="photo office" role="img" aria-label="Photo of office staff in a modern lunchroom with vending machines"></div>
    <div class="section section--a">
      <h2 class="heading tag">We stock a large range of<br>quality products</h2>
      <p class="body-text">From chilled drinks and coffee to chips, bars and fresh snacks, we carry hundreds of lines from trusted suppliers and rotate stock often so there is always something new to try.</p>
    </div>
    <div class="section section--b">
      <h2 class="heading tag">Healthier options</h2>
      <p class="body-text">We know a balanced diet matters at work. Ask for our healthy range with low sugar drinks, nuts, fruit bars and wholegrain snacks, clearly marked so staff can choose well.</p>
    </div>
  </article>

  <article class="panel free">
    <h2 class="heading tag">Free delivery · Free install<br>Free service · Free support</h2>
    <div class="photo team" role="img" aria-label="Photo of business people beside a vending machine"></div>
    <svg class="swoosh" viewBox="0 0 220 252" preserveAspectRatio="none" aria-hidden="true">
      <path d="M220 0 Q40 60 0 252 L220 252 Z" fill="var(--red)"/>
      <path d="M220 0 Q40 60 0 252 L-8 252 Q30 50 220 -10 Z" fill="var(--muted)"/>
    </svg>
    <p class="phone">1300 555 019</p>
    <p class="web">www.qorvelindustries.com.au</p>
  </article>
</section>

</body>
</html>
```